Redesign for Real Estate Lead Generation Site

We are looking for a slight redesign for our real estate lead generation sites.

Here's one of our current sites: www.qdrhousefigures.com

The design should be simple as it is currently, remain only on one page, and nothing too detailed to where it may take a while to load/reload. We also have parallel sites, www.lmnhousefigures.com, www.lmnquicklistings.com, and a few others which all will end up utilizing the same template.

We've found that the majority of the site traffic will come from print advertising, not as much SEO. But also understand the more simple the site, the greater likelihood a user may find us through search engines. Another reason we want to keep it rather simple and clean.

The content on the page needs to remain the same, but with additional spaces for one written paragraph testimonial, and an area where we can incorporate a video. Originally, the ideal spot would be the open white space below the social media logos, but we are open to different ideas as you create the redesign.

A change in colors and simple graphics is what we're looking for most along with the testimonial / video additions. Also, we have a new logo we need incorporated into the site somewhere: http://www.brennoprintworks.com/KV-Crew-Properties.zip to download the file in different formates.

Here is our main site, www.kvcrewproperties.com through wordpress, so you can get an idea of what folks go to once they've signed up and received a confirm e-mail.

Please contact us if you have any questions. Good luck and thanks for submitting!

```html
<!DOCTYPE html>
<html lang="en">
<head>
<meta charset="utf-8">
<title>KV Crew Properties – Home Value Report</title>
<link rel="stylesheet" href="https://fonts.googleapis.com/css2?family=Arimo:wght@400;700&family=Tinos&display=swap">
<style>
:root{
  --page-bg:#d8d4d2;
  --panel-white:#ffffff;
  --brand-yellow:#fbb715;
  --form-grey:#e1e7ea;
  --ink:#1d1d1d;
  --ink-soft:#444b52;
  --rule:#c9cfd3;
  --field:#ffffff;
  --dark:#231f20;
  --footer-top:#1a7fd4;
  --footer-bottom:#7cc0ef;
  --grass:#5e9a35;
}
*{box-sizing:border-box;margin:0;padding:0}
html,body{width:986px;height:1200px;overflow:hidden}
body{background:var(--page-bg);font-family:"Arimo",Arial,sans-serif;color:var(--ink);position:relative}
.abs{position:absolute}
.header-panel{left:73px;top:0;width:854px;height:474px;background:var(--panel-white)}
.brand{left:99px;top:17px;display:flex;align-items:center;gap:12px}
.brand-mark{width:58px;height:58px;background:var(--dark)}
.brand-name{font-size:26px;color:var(--dark);line-height:1}
.tagline{left:616px;top:16px;width:255px;font-family:"Tinos",Georgia,serif;font-size:22px;line-height:28px;color:#111}
.hero-photo{left:99px;top:126px;width:464px;height:326px;background:linear-gradient(180deg,#8ca36a 0%,#c9ccd0 35%,#b8b4ac 65%,#4f6b2e 100%)}
.thumb{width:149px;height:85px}
.thumb.a{background:linear-gradient(180deg,#9fb4c4,#dadcd8 50%,#5d7a3a)}
.thumb.b{background:linear-gradient(180deg,#5b8fd6,#c8c2b8 55%,#4f7a2c)}
.thumb.c{background:linear-gradient(180deg,#8fb8e4,#8a3f2e 55%,#4e7a2e)}
.thumb.d{background:linear-gradient(180deg,#d9e3e8,#4c4a48 55%,#3e6a26)}
.gallery-nav{left:580px;top:427px;width:313px;height:24px;background:var(--dark)}
.gallery-nav svg{position:absolute;top:5px}
.lower-band{left:85px;top:474px;width:831px;height:612px;background:var(--brand-yellow)}
.form-panel{left:85px;top:474px;width:382px;height:589px;background:var(--form-grey);border-radius:0 0 10px 10px}
.intro{left:107px;top:496px;width:345px;font-size:11.5px;line-height:19.3px;color:var(--ink-soft)}
.form-rule{left:94px;top:597px;width:364px;height:1px;background:var(--rule)}
.label{font-size:12px;color:var(--ink)}
.field{background:var(--field);height:17px}
.group{border:1px solid var(--rule);}
.legend{font-size:17px;color:#111;background:var(--form-grey);padding:0 6px}
.select{background:var(--field);height:17px}
.select::after{content:"";position:absolute;right:2px;top:2px;width:13px;height:13px;background:#5d5d5d}
.select span{position:absolute;right:5px;top:7px;border:3px solid transparent;border-top:4px solid #fff;z-index:1}
.signup{left:152px;top:1018px;width:76px;height:19px;border-radius:10px;background:#fff;font-size:13px;text-align:center;line-height:19px}
.section-title{font-family:"Tinos",Georgia,serif;font-size:22px;font-weight:400;color:#fff}
.quote{width:410px;font-size:11px;line-height:19.3px;color:#222}
.quote .by{display:block;text-align:right;font-weight:700;color:#111}
.band-rule{left:494px;top:742px;width:422px;height:1px;background:#fdd46e}
.video{left:494px;top:808px;width:414px;height:256px;background:#000;border-radius:8px;color:#fff;text-align:center}
.video h3{position:absolute;left:0;top:68px;width:100%;font-size:11.5px;font-weight:700}
.video small{position:absolute;left:0;top:83px;width:100%;font-size:8.5px;color:#bbb}
.video svg{position:absolute;left:169px;top:104px}
.footer{left:0;top:1086px;width:986px;height:114px;background:linear-gradient(180deg,var(--footer-top),var(--footer-bottom) 88%,var(--grass) 88%)}
.footer-photo{left:53px;top:1110px;width:178px;height:78px;background:linear-gradient(180deg,#d4dbe2,#a9a18f 60%,#5b8a34)}
.footer-info{left:240px;top:1112px;width:480px;text-align:center;color:#fff;font-size:12px;line-height:18px}
.footer-info .small{font-size:10.5px}
.phone-pill{display:inline-flex;align-items:center;gap:4px;background:#e8eef3;color:#2a4a63;border-radius:8px;padding:0 6px;font-size:10px;font-weight:700;line-height:13px;vertical-align:1px}
.phone-pill i{width:18px;height:8px;background:#8899aa;display:inline-block}
.follow{left:802px;top:1094px;font-family:"Tinos",Georgia,serif;font-size:23px;color:#fff}
.social{top:1136px;width:34px;height:34px;border-radius:4px;background:rgba(255,255,255,.85)}
</style>
</head>
<body>
<div class="abs header-panel"></div>
<div class="abs brand"><div class="brand-mark"></div><div class="brand-name">KV Crew Properties</div></div>
<p class="abs tagline">"What is the current market value of my home in today's market?"</p>
<div class="abs hero-photo" role="img" aria-label="Photo of a large stone and brick family home with landscaped front garden"></div>
<div class="abs thumb a" style="left:580px;top:128px" role="img" aria-label="Photo of a white two-storey house"></div>
<div class="abs thumb b" style="left:741px;top:128px" role="img" aria-label="Photo of a house with a for-sale sign"></div>
<div class="abs thumb c" style="left:580px;top:228px" role="img" aria-label="Photo of a red brick house with garden"></div>
<div class="abs thumb d" style="left:741px;top:229px" role="img" aria-label="Photo of a steep-roofed house among trees"></div>
<div class="abs thumb c" style="left:580px;top:329px" role="img" aria-label="Photo of a red brick house with garden"></div>
<div class="abs thumb d" style="left:741px;top:329px" role="img" aria-label="Photo of a steep-roofed house among trees"></div>
<div class="abs gallery-nav">
  <svg style="left:9px" width="14" height="14" viewBox="0 0 14 14"><path d="M10 1 4 7l6 6" fill="none" stroke="#fff" stroke-width="2.5"/></svg>
  <svg style="right:9px" width="14" height="14" viewBox="0 0 14 14"><path d="M4 1l6 6-6 6" fill="none" stroke="#fff" stroke-width="2.5"/></svg>
</div>

<div class="abs lower-band"></div>
<div class="abs form-panel"></div>
<p class="abs intro">Fill out the form below for a FREE Comparative Market Analysis Report from KV Crew Properties for an estimate of your home's current value. The more complete the form the easier it will be to provide an accurate report regarding the value of your home.</p>
<div class="abs form-rule"></div>

<span class="abs label" style="left:108px;top:619px">Name</span><div class="abs field" style="left:152px;top:618px;width:296px"></div>
<span class="abs label" style="left:108px;top:646px">Email</span><div class="abs field" style="left:152px;top:645px;width:296px"></div>
<span class="abs label" style="left:108px;top:674px">Phone</span><div class="abs field" style="left:153px;top:673px;width:295px"></div>

<div class="abs group" style="left:108px;top:724px;width:338px;height:97px"></div>
<span class="abs legend" style="left:138px;top:712px">Property Address</span>
<span class="abs label" style="left:116px;top:758px;font-size:11.5px">Street Address</span><div class="abs field" style="left:199px;top:757px;width:234px"></div>
<span class="abs label" style="left:118px;top:794px;font-size:11.5px">City</span><div class="abs field" style="left:148px;top:793px;width:72px"></div>
<span class="abs label" style="left:226px;top:794px;font-size:11.5px">State</span><div class="abs select" style="left:261px;top:793px;width:55px"><span></span></div>
<span class="abs label" style="left:325px;top:794px;font-size:11.5px">Zip</span><div class="abs field" style="left:350px;top:793px;width:83px"></div>

<div class="abs group" style="left:108px;top:866px;width:338px;height:97px"></div>
<span class="abs legend" style="left:137px;top:854px">Property Description</span>
<span class="abs label" style="left:119px;top:894px;font-size:11.5px">Number of bedroom</span><div class="abs select" style="left:233px;top:893px;width:45px"><span></span></div>
<span class="abs label" style="left:290px;top:894px;font-size:11.5px">Bathrooms</span><div class="abs select" style="left:358px;top:893px;width:76px"><span></span></div>
<span class="abs label" style="left:115px;top:922px;font-size:11.5px">Condition</span><div class="abs select" style="left:172px;top:922px;width:262px"><span></span></div>

<span class="abs label" style="left:121px;top:982px;font-size:11.5px">Additional Comments:</span>
<div class="abs field" style="left:248px;top:979px;width:185px;height:68px"></div>
<div class="abs signup">sign up!</div>

<h2 class="abs section-title" style="left:492px;top:494px">Testimonial</h2>
<p class="abs quote" style="left:496px;top:530px">Lorem ipsum dolor sit amet, consectetuer adipiscing elit, sed diam nonummy nibh euismod tincidunt ut laoreet dolore magna aliquam erat volutpat. Ut wisi enim ad minim veniam, quis nostrud exerci tation ullamcorper sus<span class="by">Mira Delcourt, CEO, Brightpath Studio</span></p>
<p class="abs quote" style="left:496px;top:633px">Lorem ipsum dolor sit amet, consectetuer adipiscing elit, sed diam nonummy nibh euismod tincidunt ut laoreet dolore magna aliquam erat volutpat. Ut wisi enim ad minim veniam, quis nostrud exerci tation ullamcorper sus<span class="by">Mira Delcourt, CEO, Brightpath Studio</span></p>
<div class="abs band-rule"></div>
<h2 class="abs section-title" style="left:496px;top:763px">Quick Intro</h2>
<div class="abs video">
  <h3>Watch video</h3>
  <small>(1 minute)</small>
  <svg width="76" height="76" viewBox="0 0 76 76">
    <circle cx="38" cy="38" r="36" fill="#2b2b2b" stroke="#777" stroke-width="3"/>
    <circle cx="38" cy="38" r="30" fill="#111"/>
    <path d="M30 24v28l23-14z" fill="#f07d1a"/>
  </svg>
</div>

<footer class="abs footer"></footer>
<div class="abs footer-photo" role="img" aria-label="Photo of a grand manor house on a lawn"></div>
<div class="abs footer-info">
  <div><span class="small">KV Crew Properties</span> :: Northgate Realty Group :: <span class="phone-pill"><i></i>866-KV-HOMES</span> ::</div>
  <div class="small" style="line-height:14px">info@kvcrewproperties.com</div>
  <div style="margin-top:6px">© 2010 KV Crew Properties</div>
</div>
<div class="abs follow">Follow us</div>
<div class="abs social" style="left:792px" aria-label="Social profile"></div>
<div class="abs social" style="left:829px" aria-label="Social profile"></div>
<div class="abs social" style="left:867px" aria-label="Social profile"></div>
<div class="abs social" style="left:905px" aria-label="Social profile"></div>
</body>
</html>
```